Real Estate Investor needs awesome business card design

I invest in real estate, focused on multi-family properties, and I need a business card to hand out to potential partners. I prefer simple, clean designs, but it needs to stand out, so I'd like there to be a bit of red in the design as well.

It should include this information:

Front
Dallin Pecksworth
Real Estate Investor
Direct phone: 502-867-3394
Email: dallinhpecksworth@quillmail.example
Headshot (Picture), I've uploaded a few, just pick the one you think looks best with your design. You can remove the background from the headshot image if it looks better.

Back
The back of the card's design should flow and be congruent with the front. On the back I want to put an inspirational quote or question. There will be different ones depending on the card, so I'll need the original file so I can edit it in the end.

For now, use “The Pessimist Sees Difficulty In Every Opportunity. The Optimist Sees The Opportunity In Every Difficulty.” -Barnaby Ellsworth

Target Market(s)

Investors

Industry/Entity Type

Real Estate

Contact Information for Business Card

Front
Dallin Pecksworth
Real Estate Investor

Back
The back of the card's design should flow and be congruent with the front. On the back I want to put an inspirational quote or question. There will be different ones depending on the card, so I'll need the original file so I can edit it in the end. I've uploaded some EXAMPLES of business cards with quotes on them. Don't copy but feel free to use them as inspiration.

The design will be printed on "ZIB sized" business cards
1039 x 697 pixels
with rounded corners

Font styles to use
Serif
Decorative
Script

Colors
ec1f27

Requirements
Must have
• Headshot, name, and other information in it.
• 1039 x 697 pixels
• Rounded corners
• Clean design that pops. I'm open to see any color background, including black.
• Headshots can be located here: https://www.filecrate.example/sh/8kd2wq7mzt31hvx/BBQTXP4ruf9LmQ0KhcvWx7b?dl=0
Nice to have
• It would be awesome if the design included a personal signature or monogram, but if not I'll get a personal logo developed later and the card redesigned if I think it needs it.
Should not have
• Cluttered design

```html
<!DOCTYPE html>
<html lang="en">
<head>
<meta charset="utf-8">
<title>Dallin Pecksworth – Business Card</title>
<link rel="stylesheet" href="https://fonts.googleapis.com/css2?family=Encode+Sans:wght@300;400&family=Fira+Sans:wght@600&display=swap">
<style>
  :root {
    --backdrop: #e2e4e5;
    --card: #171717;
    --mint: #6fd3b1;
    --mint-deep: #3f8a72;
    --accent-red: #ec1f27;
    --photo-tone: #3a3a3a;
    --photo-tone-light: #5a5a5a;
  }
  * { box-sizing: border-box; margin: 0; padding: 0; }
  html, body {
    width: 1200px;
    height: 857px;
    overflow: hidden;
    background: var(--backdrop);
  }
  .stage { position: relative; width: 1200px; height: 857px; }

  .card {
    position: absolute;
    width: 566px;
    height: 381px;
    background: var(--card);
    border-radius: 11px;
    overflow: hidden;
  }
  .card--front { left: 109px; top: 85px; }
  .card--back  { left: 517px; top: 417px; }

  /* Front */
  .pattern-panel {
    position: absolute;
    left: 0; top: 0;
    width: 270px; height: 381px;
    background: linear-gradient(135deg, var(--mint-deep), #2a5e4e 50%, var(--mint-deep));
  }
  .headshot-frame {
    position: absolute;
    left: 54px; top: 83px;
    width: 160px; height: 216px;
    border: 7px solid var(--mint);
    background: var(--card);
  }
  .headshot {
    width: 100%; height: 100%;
    background: radial-gradient(ellipse at 50% 40%, var(--photo-tone-light), var(--photo-tone) 70%);
  }
  .identity {
    position: absolute;
    left: 291px; top: 82px;
    width: 250px; height: 217px;
    border-top: 2px solid var(--mint);
    border-bottom: 2px solid var(--mint);
    color: var(--mint);
    font-family: "Encode Sans", sans-serif;
    font-weight: 300;
  }
  .identity__name {
    margin-top: 12px;
    font-family: "Encode Sans", sans-serif;
    font-weight: 300;
    font-size: 28px;
    line-height: 1.2;
    white-space: nowrap;
  }
  .identity__details {
    position: absolute;
    left: 2px; top: 128px;
    font-size: 13.5px;
    line-height: 23px;
    white-space: nowrap;
  }

  /* Back */
  .quote {
    position: absolute;
    left: 32px; top: 62px;
    color: var(--mint);
    font-family: "Fira Sans", sans-serif;
    font-weight: 600;
    font-size: 25px;
    line-height: 37.5px;
    white-space: nowrap;
  }
  .quote__mark {
    color: var(--accent-red);
    font-size: 34px;
    line-height: 0;
    position: relative;
  }
  .quote__mark--open { top: -6px; margin-right: 2px; }
  .quote__mark--close { top: 12px; margin-left: 4px; }
  .quote__author {
    position: absolute;
    right: 37px; top: 304px;
    color: var(--mint);
    font-family: "Fira Sans", sans-serif;
    font-weight: 600;
    font-size: 25px;
    white-space: nowrap;
  }
</style>
</head>
<body>
<main class="stage">
  <section class="card card--front" aria-label="Card front">
    <div class="pattern-panel" role="img" aria-label="Mint and black chevron stripe pattern"></div>
    <div class="headshot-frame">
      <div class="headshot" role="img" aria-label="Black and white headshot of Dallin Pecksworth"></div>
    </div>
    <div class="identity">
      <h1 class="identity__name">Dallin Pecksworth</h1>
      <p class="identity__details">
        Real Estate Investor<br>
        Direct phone: 502-867-3394<br>
        E: dallinhpecksworth@quillmail.example
      </p>
    </div>
  </section>

  <section class="card card--back" aria-label="Card back">
    <blockquote class="quote">
      <span class="quote__mark quote__mark--open">“</span>The Pessimist Sees Difficulty<br>
      In Every Opportunity.<br>
      The Optimist Sees The Opportunity<br>
      In Every Difficulty<span class="quote__mark quote__mark--close">”</span>
    </blockquote>
    <p class="quote__author">Barnaby Ellsworth</p>
  </section>
</main>
</body>
</html>
```